Concert Pianist Hot Foil Clear Plastic Business Card
Corveline-Hask Tonal Mgmt
Concert Pianist Hot Foil Clear Plastic Business Card - Music
Creative Brief
Use specific fonts
Use the font Freeky Typewriter (by Quillmarrow Type) for Corveline-Hask Tonal Mgmt. Use a standard fo
Cutting-Edge
Dorian Felsk
Corveline_hask Tonal Mgmt
27816 Old Quarry Road Suite 418 Saratoga, California 95071
DorianFelsk@Mirelodan.example
www.Mirelodan.example
We like this card and would recommend it as a model. http://www.lucentprintworks.example/glasshue/images/businesscards/clearcard4.jpg Here are pictures that can be used: http://s204.beta.snapvaultly.example/user/daedalwander/library/Mirelodan%20Business%20Card? We want the web site to be the most distinctive address.
Nothing on the back is required but--if you are cleaver you can place a photograph behind picture on front. You can chose from the selection provided. (All of the pictures are recent except for the B & W photograph with bow tie.) http://s204.beta.snapvaultly.example/user/daedalwander/library/Mirelodan%20Business%20Card?

```html
<!DOCTYPE html>
<html lang="en">
<head>
<meta charset="utf-8">
<title>Corveline-Hask Tonal Mgmt – Clear Plastic Business Card</title>
<link rel="stylesheet" href="https://fonts.googleapis.com/css2?family=Special+Elite&family=Cormorant+Garamond:wght@600&family=Lato:wght@400&display=swap">
<style>
  :root {
    --backdrop: #d9d4cc;
    --card-black: #0d0c0d;
    --card-edge: #2a2829;
    --foil-red: #c1232e;
    --text-white: #f1eeea;
    --photo-dark: #1b1a1b;
    --photo-light: #8d8a88;
    --keys-dark: #0b0b0b;
    --keys-clear: #b9b1a6;
  }
  html, body {
    margin: 0;
    width: 1200px;
    height: 410px;
    overflow: hidden;
    background: var(--backdrop);
  }
  .canvas {
    position: relative;
    width: 1200px;
    height: 410px;
  }
  .card {
    position: absolute;
    background: var(--card-black);
    border: 1px solid var(--card-edge);
    border-radius: 14px;
    overflow: hidden;
    box-sizing: border-box;
  }
  .card--back {
    left: 300px;
    top: 30px;
    width: 396px;
    height: 310px;
  }
  .card--front {
    left: 730px;
    top: 20px;
    width: 396px;
    height: 310px;
  }
  .keys {
    position: absolute;
    top: 0;
    bottom: 0;
    width: 92px;
    background: repeating-linear-gradient(180deg, var(--keys-dark) 0 18px, var(--keys-clear) 18px 30px);
  }
  .card--back .keys { left: 0; }
  .card--front .keys { right: 0; }
  .portrait {
    position: absolute;
    left: 120px;
    top: 20px;
    width: 240px;
    height: 270px;
    background: radial-gradient(ellipse at 50% 40%, var(--photo-light), var(--photo-dark) 70%);
  }
  .brand {
    position: absolute;
    left: 26px;
    top: 28px;
    width: 240px;
    font-family: "Special Elite", monospace;
    font-size: 20px;
    line-height: 1.15;
    letter-spacing: 1px;
    color: var(--text-white);
    text-transform: uppercase;
    margin: 0;
  }
  .contact {
    position: absolute;
    left: 26px;
    top: 112px;
    width: 260px;
  }
  .name {
    font-family: "Cormorant Garamond", serif;
    font-weight: 600;
    font-size: 24px;
    line-height: 1;
    color: var(--foil-red);
    margin: 0;
  }
  .role {
    font-family: "Lato", sans-serif;
    font-size: 11px;
    color: var(--foil-red);
    margin: 4px 0 22px;
  }
  .details {
    font-family: "Lato", sans-serif;
    font-size: 10px;
    line-height: 1.6;
    color: var(--text-white);
    margin: 0;
  }
  .details .web { font-size: 12px; }
</style>
</head>
<body>
<main class="canvas">
  <section class="card card--back" aria-label="Card back">
    <div class="keys" role="img" aria-label="Piano key pattern along the card edge"></div>
    <div class="portrait" role="img" aria-label="Black and white portrait of the pianist in a bow tie"></div>
  </section>

  <section class="card card--front" aria-label="Card front">
    <div class="keys" role="img" aria-label="Piano key pattern along the card edge"></div>
    <p class="brand">Corveline-Hask<br>Tonal Mgmt</p>
    <div class="contact">
      <h1 class="name">Dorian Felsk</h1>
      <p class="role">Concert Pianist</p>
      <p class="details">
        27816 Old Quarry Road Suite 418<br>
        Saratoga, California 95071<br>
        DorianFelsk@Mirelodan.example<br>
        <span class="web">www.Mirelodan.example</span>
      </p>
    </div>
  </section>
</main>
</body>
</html>
```